Aerial Imaging and photgraphy business card

Design a business card with eye catching aerial photo of country side / landscape with a drone in the foreground.
Also contact details.

Target Market(s)

Aerial Imaging photography

Industry/Entity Type

Advertising

Contact Information for Business Card

Corwin
0412905316
Website http://www.skylarkvistas.com.au/
email address : skylarkvistas.com.au

Colors
e8f1ca
cadf82
9bcb3c
33a6d7
85cae6
cee9f5

Requirements
Must have
• High res photo
• KPV drone in the foreground Either T4200 and kpv Hovera or both
Nice to have
• high resolution landscape country photo on the front of the card with a KPV T4200 drone in the foreground.

```html
<!DOCTYPE html>
<html lang="en">
<head>
<meta charset="utf-8">
<title>Skylark Vistas – Business Card Concepts</title>
<link rel="stylesheet" href="https://fonts.googleapis.com/css2?family=Roboto+Condensed:wght@400;700&family=Roboto+Slab:wght@500&display=swap">
<style>
  :root {
    --green: #9bcb3c;
    --green-bar: #a6c752;
    --green-soft: #cadf82;
    --blue: #33a6d7;
    --blue-mid: #85cae6;
    --blue-pale: #cee9f5;
    --ink: #22303a;
    --white: #ffffff;
    --sky: #b9d3e6;
    --field: #5d7a45;
  }
  * { box-sizing: border-box; margin: 0; padding: 0; }
  html, body { width: 846px; height: 1200px; overflow: hidden; background: var(--white); }
  body { position: relative; font-family: "Roboto Condensed", Arial, sans-serif; }

  .card { position: absolute; width: 390px; height: 223px; overflow: hidden; background: var(--white); }
  .card--wide { width: 391px; }
  .card svg.bg { position: absolute; inset: 0; width: 100%; height: 100%; }

  .row-1 { top: 75px; } .row-2 { top: 357px; } .row-3 { top: 654px; } .row-4 { top: 942px; }
  .col-front { left: 29px; } .col-back { left: 448px; } .col-back-wide { left: 454px; }

  .brand { position: absolute; display: flex; align-items: center; justify-content: center;
           text-align: center; font-weight: 700; font-size: 17px; line-height: 1.05;
           color: var(--ink); text-transform: uppercase; }
  .brand--disc { border-radius: 50%; background: var(--white); }

  .name-bar { position: absolute; height: 24px; background: var(--green-bar); color: var(--white);
              font-weight: 700; font-size: 17px; letter-spacing: .5px; line-height: 24px;
              padding-left: 22px; }
  .name-bar--right { text-align: center; padding-left: 0; }

  .contacts { position: absolute; list-style: none; font-size: 9.5px; color: var(--blue); }
  .contacts li { display: flex; align-items: center; gap: 4px; height: 14px; }
  .contacts svg { width: 9px; height: 9px; fill: var(--green); }
  .contacts--right li { justify-content: flex-end; }

  .name-slab { position: absolute; font-family: "Roboto Slab", Georgia, serif; font-weight: 500;
               font-size: 26px; color: var(--white); letter-spacing: 1px; }
  .contacts--boxed { color: var(--white); font-family: "Roboto Slab", Georgia, serif; font-size: 9.5px; }
  .contacts--boxed li { height: 13px; gap: 6px; }
  .contacts--boxed .icon-box { width: 24px; height: 11px; background: var(--blue);
                               display: flex; align-items: center; justify-content: flex-end; padding-right: 2px; }
  .contacts--boxed svg { fill: var(--white); width: 8px; height: 8px; }

  .edge-tab { position: absolute; width: 14px; height: 52px; background: var(--blue); }
  .base-bar { position: absolute; left: 0; right: 0; bottom: 0; height: 4px; background: var(--blue); }
</style>
</head>
<body>

<svg width="0" height="0" style="position:absolute" aria-hidden="true">
  <defs>
    <linearGradient id="landscape" x1="0" y1="0" x2="0" y2="1">
      <stop offset="0" stop-color="#cfe0ee"/>
      <stop offset=".3" stop-color="#a9bfcf"/>
      <stop offset=".38" stop-color="#6f8a5a"/>
      <stop offset=".7" stop-color="#4f6e3c"/>
      <stop offset="1" stop-color="#5a7446"/>
    </linearGradient>
    <linearGradient id="landscape-soft" x1="0" y1="0" x2="1" y2="1">
      <stop offset="0" stop-color="#c7d9e8"/>
      <stop offset=".35" stop-color="#7d9470"/>
      <stop offset=".65" stop-color="#8fa5a8"/>
      <stop offset="1" stop-color="#61794a"/>
    </linearGradient>
    <radialGradient id="drone" cx=".5" cy=".5" r=".5">
      <stop offset="0" stop-color="#2a2526"/>
      <stop offset=".6" stop-color="#3a2c2c" stop-opacity=".8"/>
      <stop offset="1" stop-color="#3a2c2c" stop-opacity="0"/>
    </radialGradient>
    <symbol id="i-phone" viewBox="0 0 10 10"><path d="M2 0h2l1 3-1.5 1a6 6 0 0 0 2.5 2.5L7 5l3 1v2l-1 2C4 10 0 6 0 1z"/></symbol>
    <symbol id="i-globe" viewBox="0 0 10 10"><circle cx="5" cy="5" r="5"/><path d="M0 5h10M5 0v10" stroke="#fff" stroke-width=".8"/></symbol>
    <symbol id="i-mail" viewBox="0 0 10 10"><rect y="2" width="10" height="7"/><path d="M0 2l5 4 5-4" stroke="#fff" stroke-width=".8" fill="none"/></symbol>
  </defs>
</svg>

<!-- Concept 1 -->
<section class="card row-1 col-front">
  <svg class="bg" viewBox="0 0 390 223" role="img" aria-label="Aerial photo of green countryside beside a lake with a drone in the foreground">
    <rect width="390" height="223" fill="var(--green-bar)"/>
    <path d="M162 0Q112 111 158 223H390V0Z" fill="url(#landscape)"/>
    <path d="M162 0Q112 111 158 223" stroke="#fff" stroke-width="5" fill="none"/>
    <ellipse cx="290" cy="80" rx="80" ry="40" fill="url(#drone)"/>
  </svg>
  <div class="brand brand--disc" style="left:14px;top:59px;width:94px;height:94px;">Skylark Vistas</div>
</section>

<section class="card row-1 col-back">
  <svg class="bg" viewBox="0 0 390 223" role="img" aria-label="Aerial photo of a lake shore with a hovering drone">
    <path d="M218 0Q166 111 218 223H390V0Z" fill="var(--blue)"/>
    <path d="M232 0Q182 111 230 223H390V0Z" fill="url(#landscape)"/>
    <ellipse cx="255" cy="85" rx="95" ry="40" fill="url(#drone)"/>
  </svg>
  <div class="brand" style="left:12px;top:14px;width:100px;height:100px;">Skylark Vistas</div>
  <div class="name-bar" style="left:0;top:133px;width:144px;">CORWIN</div>
  <ul class="contacts" style="left:22px;top:164px;">
    <li><svg><use href="#i-phone"/></svg>0412905316</li>
    <li><svg><use href="#i-globe"/></svg>http://www.skylarkvistas.com.au/</li>
    <li><svg><use href="#i-mail"/></svg>skylarkvistas.com.au</li>
  </ul>
</section>

<!-- Concept 2 -->
<section class="card row-2 col-front">
  <svg class="bg" viewBox="0 0 390 223" role="img" aria-label="Soft-focus aerial photo of countryside and lake">
    <rect width="390" height="223" fill="url(#landscape-soft)"/>
    <circle cx="188" cy="113" r="54" fill="none" stroke="#fff" stroke-width="2"/>
  </svg>
  <div class="brand brand--disc" style="left:143px;top:68px;width:90px;height:90px;">Skylark Vistas</div>
  <span class="edge-tab" style="left:0;top:88px;"></span>
  <span class="edge-tab" style="right:0;top:88px;"></span>
</section>

<section class="card row-2 col-back">
  <svg class="bg" viewBox="0 0 390 223" role="img" aria-label="Aerial photo of countryside under a green tint with a drone">
    <rect width="390" height="223" fill="url(#landscape-soft)"/>
    <rect x="10" y="8" width="370" height="207" fill="var(--green)" opacity=".6"/>
    <ellipse cx="270" cy="100" rx="90" ry="45" fill="url(#drone)"/>
  </svg>
  <div class="brand brand--disc" style="left:26px;top:24px;width:88px;height:88px;">Skylark Vistas</div>
  <div class="name-slab" style="left:26px;top:122px;">CORWIN</div>
  <ul class="contacts contacts--boxed" style="left:8px;top:162px;">
    <li><span class="icon-box"><svg><use href="#i-phone"/></svg></span>0412905316</li>
    <li><span class="icon-box"><svg><use href="#i-globe"/></svg></span>http://www.skylarkvistas.com.au/</li>
    <li><span class="icon-box"><svg><use href="#i-mail"/></svg></span>skylarkvistas.com.au</li>
  </ul>
  <span class="edge-tab" style="right:0;top:86px;"></span>
</section>

<!-- Concept 3 -->
<section class="card row-3 col-front">
  <svg class="bg" viewBox="0 0 390 223" role="img" aria-label="Soft-focus aerial landscape with blue diagonal tints">
    <rect width="390" height="223" fill="url(#landscape-soft)"/>
    <polygon points="0,72 68,72 192,223 0,223" fill="#1d6f9a" opacity=".55"/>
    <polygon points="265,72 390,72 390,223 360,223" fill="var(--blue)" opacity=".55"/>
    <polygon points="180,0 390,0 390,72 250,72" fill="#fff" opacity=".12"/>
  </svg>
  <div class="brand brand--disc" style="left:154px;top:64px;width:94px;height:94px;">Skylark Vistas</div>
</section>

<section class="card card--wide row-3 col-back-wide">
  <svg class="bg" viewBox="0 0 391 223" role="img" aria-label="Aerial photo of lake country with a drone in the foreground">
    <polygon points="100,0 118,0 391,205 391,223" fill="var(--blue)"/>
    <polygon points="118,0 391,0 391,205" fill="url(#landscape)"/>
    <ellipse cx="265" cy="90" rx="90" ry="45" fill="url(#drone)"/>
  </svg>
  <div class="brand" style="left:28px;top:30px;width:100px;height:90px;">Skylark Vistas</div>
  <div class="name-bar" style="left:0;top:138px;width:155px;padding-left:32px;">CORWIN</div>
  <ul class="contacts" style="left:30px;top:169px;">
    <li><svg><use href="#i-phone"/></svg>0412905316</li>
    <li><svg><use href="#i-globe"/></svg>http://www.skylarkvistas.com.au/</li>
    <li><svg><use href="#i-mail"/></svg>skylarkvistas.com.au</li>
  </ul>
</section>

<!-- Concept 4 -->
<section class="card row-4 col-front">
  <svg class="bg" viewBox="0 0 390 223" role="img" aria-label="Soft-focus aerial photo of countryside and lake">
    <rect width="390" height="223" fill="url(#landscape-soft)"/>
  </svg>
  <div class="brand brand--disc" style="left:140px;top:56px;width:112px;height:112px;">Skylark Vistas</div>
  <span class="base-bar"></span>
</section>

<section class="card card--wide row-4 col-back-wide">
  <svg class="bg" viewBox="0 0 391 223" role="img" aria-label="Aerial photo of green hills with a drone in the foreground">
    <polygon points="0,0 232,0 150,219 0,219" fill="url(#landscape)"/>
    <ellipse cx="130" cy="110" rx="100" ry="45" fill="url(#drone)"/>
  </svg>
  <div class="brand" style="left:272px;top:20px;width:96px;height:80px;">Skylark Vistas</div>
  <div class="name-bar name-bar--right" style="left:253px;top:126px;width:138px;">CORWIN</div>
  <ul class="contacts contacts--right" style="right:17px;top:153px;">
    <li>0412905316<svg><use href="#i-phone"/></svg></li>
    <li>http://www.skylarkvistas.com.au/<svg><use href="#i-globe"/></svg></li>
    <li>skylarkvistas.com.au<svg><use href="#i-mail"/></svg></li>
  </ul>
  <span class="base-bar"></span>
</section>

</body>
</html>
```